Simple Floral Service Web-Banner

I need to put a banner add on the members section of a website for an organization in which we are members.

The ad size is 470px x 214px.

I am uploading 4 pictures. 1 is a picture of red roses, and 1 is a picture of a t-shirt. These are 2 major products of ours which need to be incorporated in the banner. I do not have these in higher res or vectorized format, so please work with what you have. I am also uploading our 2 logos, one is for our Canadian company, and one for our American company. Both logos should be included at equal sizes.

The following text should be used:
"Proudly providing top quality roses, and custom commemorative grad t-shirts at over 800 schools."

I am just looking for a simple banner incorporating those pictures and that wording. I don't want something that is overly flashy.

I will monitor the submissions in a timely manner and give you feedback.

```html
<!DOCTYPE html>
<html lang="en">
<head>
<meta charset="UTF-8">
<title>Laurel Blooms – Roses and Grad T-Shirts Banner</title>
<link href="https://fonts.googleapis.com/css2?family=Open+Sans:wght@400;600;700&display=swap" rel="stylesheet">
<style>
  :root {
    --ink: #555a5c;
    --ink-dark: #2f3233;
    --rose-red: #b3202d;
    --leaf-green: #7c9b3b;
    --button-green: #8fb35b;
    --paper: #ffffff;
    --divider: #c9c9c9;
    --rose-deep: #8e1420;
    --rose-mid: #c4343a;
    --wood: #8a5a3a;
    --shirt-light: #f1f1f1;
    --shirt-shade: #cfd0d0;
  }
  html, body {
    margin: 0;
    padding: 0;
    width: 1200px;
    height: 1077px;
    overflow: hidden;
    background: var(--paper);
    font-family: "Open Sans", Arial, sans-serif;
  }
  .canvas {
    position: relative;
    width: 1200px;
    height: 1077px;
  }
  .banner {
    position: absolute;
    left: 0;
    width: 1200px;
    background: var(--paper);
    overflow: hidden;
  }
  .banner--roses { top: 0; height: 530px; }
  .banner--shirts { top: 538px; height: 539px; }
  .divider {
    position: absolute;
    left: 0;
    top: 532px;
    width: 1200px;
    height: 3px;
    background: var(--divider);
  }
  .brand {
    position: absolute;
    left: 41px;
    display: flex;
    align-items: center;
    gap: 12px;
    color: var(--leaf-green);
    font-weight: 600;
    font-size: 38px;
    line-height: 1;
    letter-spacing: -0.5px;
  }
  .brand__dot {
    width: 18px;
    height: 18px;
    border-radius: 50%;
    background: var(--leaf-green);
  }
  .banner--roses .brand { top: 28px; }
  .banner--shirts .brand { top: 24px; }
  .headline {
    position: absolute;
    left: 41px;
    margin: 0;
    color: var(--ink);
    font-weight: 400;
    letter-spacing: -0.5px;
  }
  .banner--roses .headline {
    top: 138px;
    font-size: 66px;
    line-height: 86px;
  }
  .banner--shirts .headline {
    top: 112px;
    font-size: 56px;
    line-height: 66px;
  }
  .headline .accent-red { color: var(--rose-red); font-weight: 700; }
  .headline .accent-green { color: var(--leaf-green); font-weight: 700; }
  .headline .big {
    display: block;
    color: var(--ink-dark);
    font-weight: 700;
    font-size: 76px;
    line-height: 90px;
  }
  .shop-button {
    position: absolute;
    left: 41px;
    width: 220px;
    height: 72px;
    display: flex;
    align-items: center;
    padding-left: 24px;
    box-sizing: border-box;
    background: var(--button-green);
    color: var(--paper);
    font-size: 31px;
    font-weight: 600;
    text-decoration: none;
    letter-spacing: -0.5px;
    clip-path: polygon(0 0, 84% 0, 100% 50%, 84% 100%, 0 100%);
  }
  .banner--roses .shop-button { top: 388px; }
  .banner--shirts .shop-button { top: 400px; }
  .product-photo {
    position: absolute;
    top: 0;
    right: 0;
    height: 100%;
  }
  .product-photo--roses {
    left: 600px;
    background:
      radial-gradient(ellipse at 55% 45%, var(--rose-mid) 0%, var(--rose-deep) 40%, #3f5a2a 62%, transparent 75%),
      linear-gradient(180deg, #efe6dc 0%, #e4d6c8 55%, var(--wood) 75%, #6a3f26 100%);
    clip-path: polygon(190px 0, 100% 0, 100% 100%, 0 100%);
  }
  .product-photo--shirts {
    left: 600px;
    background:
      radial-gradient(ellipse at 50% 50%, var(--shirt-light) 0%, #e6e6e6 45%, var(--shirt-shade) 80%),
      linear-gradient(180deg, #f4f4f4, #dcdcdc);
    clip-path: polygon(240px 0, 100% 0, 100% 100%, 0 100%);
  }
</style>
</head>
<body>
  <main class="canvas">
    <section class="banner banner--roses">
      <div class="brand"><span class="brand__dot"></span>Laurel Blooms</div>
      <h1 class="headline">Proudly providing<br>top quality <span class="accent-red">roses</span></h1>
      <a class="shop-button" href="#">Shop Now</a>
      <div class="product-photo product-photo--roses" role="img" aria-label="Photo of a bouquet of red roses with baby's breath wrapped in paper on a wooden table"></div>
    </section>

    <div class="divider"></div>

    <section class="banner banner--shirts">
      <div class="brand"><span class="brand__dot"></span>Laurel Blooms</div>
      <h2 class="headline">Custom commemorative<br>grad <span class="accent-green">t-shirts</span> at over<span class="big">800 schools</span></h2>
      <a class="shop-button" href="#">Shop Now</a>
      <div class="product-photo product-photo--shirts" role="img" aria-label="Photo of two white commemorative graduation t-shirts, front with school crest and back listing the graduating class"></div>
    </section>
  </main>
</body>
</html>
```